Re jig a A4 Instructional Flyer

We need an established A4 instructional Flyer (2 pages x A4) - to be rejigged in Harlow Academy of Learning Branding to look fresh and new.

Permissions have been received to rejig this Medical Triage Chart. Fresh branding and setting out (fonts) required.

FOOTER NOTES : to be inserted at the bottom of the A4 instruction sheet

Harlow Academy produced with permissions from Coastal Care Alliance, produced by Coastal Care Alliance with Clinic Circle Eastgate with permissions from Southern Basin Careline Hub. Harlow acknowledges the FMPCB Standards Criterion 3.2.3 Practice Training and Education in Triage

Target Market(s)

Medical Practices

Industry/Entity Type

Health

Font styles to use
Serif

Colors
0255a3
f78f20

Requirements
Must have
• Professional
• Pops of colour in the chart.
• This chart is to be USED and is VISUAL (no boring grey words throughout)
• PROBS SANS SERIF but SERIF for titles OK
Nice to have
• look at www.harlowlearning.edu.au FOR BRANDING look and feel

```html
<!DOCTYPE html>
<html lang="en">
<head>
<meta charset="utf-8">
<title>Triage – A guide to urgency for non-clinical staff</title>
<link rel="stylesheet" href="https://fonts.googleapis.com/css2?family=Figtree:ital,wght@0,400;0,500;0,600;0,700;0,800;0,900;1,400&display=swap">
<style>
  :root{
    --navy:#324766;
    --band:#cf8f3d;
    --ink:#1f1f24;
    --grey-box:#e3e3e8;
    --alert:#e0262a;
    --alert-bg:#f6e2dc;
    --instr:#8cc864;  --instr-bg:#eef5e6;
    --c1:#8a5aa6;     --c1-bg:#ebe2ee;
    --c2:#5b9bd5;     --c2-bg:#dde6f3;
    --c3:#5bbf9e;     --c3-bg:#d5ebe3;
    --c4:#ecc13c;     --c4-bg:#f7e8c2;
    --c5:#ea8a2a;     --c5-bg:#f4c99a;
    --c6:#d8506e;     --c6-bg:#e6a1ad;
  }
  *{box-sizing:border-box;margin:0;padding:0}
  html,body{width:1200px;height:848px;overflow:hidden;background:#fff}
  body{position:relative;font-family:"Figtree",Arial,sans-serif;color:var(--ink);font-size:12px;line-height:1.1}

  .brand{position:absolute;left:0;top:0;width:220px;height:148px;display:flex;align-items:center;justify-content:center;gap:8px;padding:0 14px}
  .brand-dot{width:14px;height:14px;border-radius:50%;background:var(--navy);flex:none}
  .brand-name{font-weight:700;color:var(--navy);font-size:15px;line-height:1.2;text-transform:uppercase;letter-spacing:.5px}

  .masthead{position:absolute;left:220px;top:0;width:980px;height:134px;background:var(--navy);color:#fff;padding:20px 0 0 46px}
  .masthead h1{font-weight:600;font-size:31px;line-height:1.25;letter-spacing:-.1px}
  .masthead h1 strong{font-weight:900;font-size:42px;letter-spacing:.5px}
  .accent-band{position:absolute;left:220px;top:134px;width:980px;height:14px;background:var(--band)}

  .flow-box{position:absolute;background:var(--grey-box);font-size:13px;display:flex;align-items:center}
  .q-urgent{left:51px;top:182px;width:234px;height:34px;padding-left:16px}
  .q-unsure{left:91px;top:237px;width:146px;height:26px;justify-content:center}
  .q-next{left:51px;top:286px;width:234px;height:40px;padding-left:12px;line-height:1.2}
  .ans{width:44px;justify-content:center;font-weight:700}
  .ans-yes{left:315px;top:182px;height:34px}
  .ans-no{left:315px;top:286px;height:40px}
  .record{left:398px;top:182px;width:378px;height:144px;display:block;padding:16px 0 0 12px}
  .record h2{font-size:13px;font-weight:700;margin-bottom:4px}
  .record li,.alert li{list-style:none;font-size:12.6px;line-height:15.4px;white-space:nowrap}
  .record li::before,.alert li::before{content:"· "}
  .arrow{position:absolute}

  .alert{position:absolute;left:794px;top:183px;width:354px;height:143px;background:var(--alert-bg);border:2px solid var(--alert);padding:14px 0 0 12px}
  .alert h2{color:var(--alert);font-size:13px;font-weight:800;margin-bottom:4px}
  .alert .call{color:var(--alert);font-weight:800;font-size:13px;margin-top:12px}

  .chart{position:absolute;left:51px;top:355px;width:1097px;display:grid;grid-template-columns:repeat(7,1fr);column-gap:5px;grid-template-rows:37px 201px 54px 47px 46px;row-gap:4px}
  .chart > div{padding:10px 6px 0 14px}
  .chart .head{color:#fff;font-weight:800;font-size:14px;display:flex;align-items:center;justify-content:center;padding:0;letter-spacing:.3px}
  .chart .criteria{padding:11px 6px 0 10px}
  .chart ul{list-style:none}
  .chart li{position:relative;padding-left:10px;margin-bottom:3px;font-size:12px;line-height:12.6px}
  .chart li::before{content:"·";position:absolute;left:0}
  .chart .action{text-align:center;font-weight:700;padding:10px 4px 0;line-height:13px;font-size:12px}
  .chart .label{font-size:12px;line-height:13px;padding-left:13px}
  .h-instr{background:var(--instr)} .b-instr{background:var(--instr-bg)}
  .h-c1{background:var(--c1)} .b-c1{background:var(--c1-bg)}
  .h-c2{background:var(--c2)} .b-c2{background:var(--c2-bg)}
  .h-c3{background:var(--c3)} .b-c3{background:var(--c3-bg)}
  .h-c4{background:var(--c4)} .b-c4{background:var(--c4-bg)}
  .h-c5{background:var(--c5)} .b-c5{background:var(--c5-bg)}
  .h-c6{background:var(--c6)} .b-c6{background:var(--c6-bg)}

  .footer{position:absolute;left:0;top:790px;width:1200px;height:58px;background:var(--navy);color:#fff;font-size:9.5px;line-height:12px}
  .disclaimer{position:absolute;left:28px;top:19px}
  .credits{position:absolute;left:557px;top:19px;width:625px;font-style:italic;color:#d6dbe4}
</style>
</head>
<body>

<div class="brand"><span class="brand-dot"></span><span class="brand-name">Harlow Academy<br>of Learning</span></div>

<header class="masthead">
  <h1><strong>TRIAGE:</strong> A guide to urgency for non-clinical staff in<br>general practice for telephone and walk in presentations</h1>
</header>
<div class="accent-band"></div>

<div class="flow-box q-urgent">Do you have an urgent problem?</div>
<div class="flow-box ans ans-yes">YES</div>
<div class="flow-box q-unsure">NO/I DON’T KNOW</div>
<div class="flow-box q-next">The next available appointment is…<br>Is this ok?</div>
<div class="flow-box ans ans-no">NO</div>

<svg class="arrow" style="left:288px;top:191px" width="26" height="16" viewBox="0 0 26 16"><path d="M0 8H23M17 2L23 8L17 14" fill="none" stroke="#111" stroke-width="1.6"/></svg>
<svg class="arrow" style="left:366px;top:191px" width="26" height="16" viewBox="0 0 26 16"><path d="M0 8H23M17 2L23 8L17 14" fill="none" stroke="#111" stroke-width="1.6"/></svg>
<svg class="arrow" style="left:288px;top:298px" width="26" height="16" viewBox="0 0 26 16"><path d="M0 8H23M17 2L23 8L17 14" fill="none" stroke="#111" stroke-width="1.6"/></svg>
<svg class="arrow" style="left:366px;top:298px" width="26" height="16" viewBox="0 0 26 16"><path d="M0 8H23M17 2L23 8L17 14" fill="none" stroke="#111" stroke-width="1.6"/></svg>
<svg class="arrow" style="left:150px;top:218px" width="16" height="18" viewBox="0 0 16 18"><path d="M8 0V16M2 10L8 16L14 10" fill="none" stroke="#111" stroke-width="1.6"/></svg>
<svg class="arrow" style="left:150px;top:266px" width="16" height="18" viewBox="0 0 16 18"><path d="M8 0V16M2 10L8 16L14 10" fill="none" stroke="#111" stroke-width="1.6"/></svg>

<div class="flow-box record">
  <h2>Record the patient’s phone number</h2>
  <ul>
    <li>What is the name and age of the patient?</li>
    <li>What is the natere of the problem?</li>
    <li>What is the duration of the problem?</li>
    <li>What is the severity of the problem?</li>
    <li>Has the patient had any previous major health problems?</li>
    <li>Select a category below and follow instructions.</li>
  </ul>
</div>

<section class="alert">
  <h2>EMERGENCY ACTION PLAN</h2>
  <ul>
    <li>Remain calm and do not panic.</li>
    <li>Be aware and respond to the needs of the emergency.</li>
    <li>Assess which patient needs to take priority.</li>
    <li>Deal with any injury or illness in order of severity.</li>
  </ul>
  <p class="call">CALL 000 FOR AMBULANCE, POLICE OR FIRE</p>
</section>

<section class="chart">
  <div class="head h-instr">INSTRUCTION</div>
  <div class="head h-c1">CATEGORY 1</div>
  <div class="head h-c2">CATEGORY 2</div>
  <div class="head h-c3">CATEGORY 3</div>
  <div class="head h-c4">CATEGORY 4</div>
  <div class="head h-c5">CATEGORY 5</div>
  <div class="head h-c6">CATEGORY 6</div>

  <div class="criteria label b-instr">Practice to ask the patient or caller to describe the problem/s, and categorise accordingly:</div>
  <div class="criteria b-c1"><ul>
    <li>Chest pain</li><li>Breathing difficulties/ trouble talking</li><li>Facial swelling and rash</li><li>Collapse/altered consciousness</li><li>Facial/limb weakness</li><li>Extensive burns</li><li>Sick patient you have concerns about</li></ul></div>
  <div class="criteria b-c2"><ul>
    <li>Fitting</li><li>Bleeding (heavy or persistent)</li><li>Spinal or head injury/ trauma</li><li>Snake bite</li><li>Heart palpitations</li><li>In labour/ruptured membranes</li><li>Neck stiffness/altered consciousness</li></ul></div>
  <div class="criteria b-c3"><ul>
    <li>Unable to urinate</li><li>Unwell ‘floppy’ infant</li><li>Poisoning/overdose</li><li>Eye injuries/chemical in the eye</li><li>Pain (severe)</li><li>Injured limb/possible fracture</li></ul></div>
  <div class="criteria b-c4"><ul>
    <li>Unwell child/elderly with fever, vomiting, diarrhoea or pain for &gt;24 hours</li><li>Pregnancy: pain or bleeding; reduced foetal movement</li><li>Abuse or assault</li><li>Visual disturbance</li><li>Patient or carer with extreme concern</li><li>Psychological distress</li></ul></div>
  <div class="criteria b-c5"><ul>
    <li>Unwell child/elderly with fever, vomiting, diarrhoea or pain for &lt;24 hours</li><li>Rash (severe)</li><li>Cut/laceration</li><li>Severe flu like symptoms</li></ul></div>
  <div class="criteria b-c6"><ul>
    <li>Adult with fever, but otherwise well</li><li>Post op problems</li><li>Eye or ear infections/ pain</li><li>Adult with continuous vomiting and/or diarrhoea for &gt;24 hrs</li></ul></div>

  <div class="label b-instr">Tell the caller to:</div>
  <div class="action b-c1">Call 000</div>
  <div class="action b-c2">Go to emergency<br>department now</div>
  <div class="action b-c3">Put call through to<br>nurse/doctor</div>
  <div class="action b-c4">Come to surgery now<br>Advise the on-call<br>nurse/doctor</div>
  <div class="action b-c5">Come to surgery today<br>and call back if gets<br>worse</div>
  <div class="action b-c6">Make an appointment<br>within 24 hours and<br>call back if gets worse</div>

  <div class="label b-instr">Practice/ Receptionist</div>
  <div class="action b-c1">Call nurse/doctor for<br>help immediately</div>
  <div class="action b-c2">Interrupt nurse/doctor<br>immediately</div>
  <div class="action b-c3">Advise nurse/doctor</div>
  <div class="action b-c4">Discuss with nurse/<br>doctor</div>
  <div class="action b-c5">Inform nurse/doctor<br>within 30 minutes</div>
  <div class="action b-c6">Inform nurse/doctor</div>

  <div class="label b-instr">Practice/ Receptionist</div>
  <div class="action b-c1">Retrieve patient file<br>Document activity</div>
  <div class="action b-c2">Retrieve patient file<br>Document activity</div>
  <div class="action b-c3">Retrieve patient file<br>Document activity</div>
  <div class="action b-c4">Retrieve patient file<br>Document activity</div>
  <div class="action b-c5">Retrieve patient file<br>Document activity</div>
  <div class="action b-c6">Retrieve patient file<br>Document activity</div>
</section>

<footer class="footer">
  <p class="disclaimer">Whilst all care has been taken in preparing this document,<br>this information is a guide only and subject to change without notice.</p>
  <p class="credits">Harlow Academy produced with permissions from Coastal Care Alliance, produced by Coastal Care Alliance with Clinic Circle Eastgate with permissions from Southern Basin Careline Hub. Harlow acknowledges the FMPCB Standards Criterion 3.2.3 Practice Training and Education in Triage.</p>
</footer>

</body>
</html>
```